IT Business Card Design

My company is a newly started small IT repair business. I operate outside of usual hours except for Saturday.
I am a very experienced and professional Technician.
I would like the business card to express that I am running a professional business and not some home IT business. This should be expressed through the design of the business card.
On the back of the card I would like the name of the company to be displayed.
Updates
Sorry guys, I have updated the requirement to be double sided. Fantastic submissions so far! Keep up the good work.
Hey designers!
Hey Designers!
Thank you all for your hard work!
Target Market(s)
Home to small business users.
Industry/Entity Type
Business
Contact Information for Business Card
Harbourline Computers
Tobin Quarle (Director)
tobin.quarle@quenmail.com.au
Operating Hours
5pm-12am Mon - Fri
9am - 5pm Sat
Mobile
0437915263
Requirements
Must have
- The base colour must be matte black. There must be some dark purple. (To go with the "Harbourline" theme)

```html
<!DOCTYPE html>
<html lang="en">
<head>
<meta charset="utf-8">
<title>Tobin Quarle – Business Card</title>
<link rel="stylesheet" href="https://fonts.googleapis.com/css2?family=Cabin:wght@400;500&family=Arimo:ital@0;1&display=swap">
<style>
  :root {
    --card-black: #000000;
    --text-white: #ffffff;
    --accent-purple: #b02ee6;
    --label-purple: #9a2ad6;
    --orb-light: #e58bff;
    --orb-mid: #b53cf0;
    --orb-dark: #5a0f8a;
  }
  html, body {
    margin: 0;
    padding: 0;
    width: 1200px;
    height: 741px;
    overflow: hidden;
    background: var(--card-black);
  }
  .card {
    position: relative;
    width: 1200px;
    height: 741px;
    background: var(--card-black);
    overflow: hidden;
  }
  .card__orb {
    position: absolute;
    left: 0;
    top: 0;
    width: 1200px;
    height: 741px;
  }
  .card__name {
    position: absolute;
    left: 137px;
    top: 170px;
    margin: 0;
    font-family: "Cabin", sans-serif;
    font-weight: 500;
    font-size: 46px;
    line-height: 1.1;
    color: var(--text-white);
  }
  .card__role {
    position: absolute;
    left: 137px;
    top: 229px;
    margin: 0;
    font-family: "Cabin", sans-serif;
    font-weight: 500;
    font-size: 40px;
    line-height: 1.1;
    color: var(--text-white);
  }
  .hours {
    position: absolute;
    left: 138px;
    top: 306px;
    margin: 0;
    font-family: "Arimo", sans-serif;
    font-size: 31px;
    line-height: 41px;
    color: var(--text-white);
  }
  .hours__title {
    display: block;
    font-style: italic;
    color: var(--accent-purple);
  }
  .hours__day { font-style: italic; }
  .contact {
    position: absolute;
    left: 138px;
    top: 550px;
    margin: 0;
    font-family: "Arimo", sans-serif;
    font-size: 31px;
    line-height: 41px;
    color: var(--text-white);
  }
  .contact__label { color: var(--label-purple); }
</style>
</head>
<body>
  <main class="card">
    <svg class="card__orb" viewBox="0 0 1200 741" role="img" aria-label="Glowing purple power button graphic">
      <defs>
        <radialGradient id="orbHalo" cx="955" cy="430" r="325" gradientUnits="userSpaceOnUse">
          <stop offset="0.6" stop-color="#6a6a6a" stop-opacity="0.55"/>
          <stop offset="1" stop-color="#000000" stop-opacity="0"/>
        </radialGradient>
        <radialGradient id="orbFill" cx="955" cy="400" r="245" gradientUnits="userSpaceOnUse">
          <stop offset="0" stop-color="var(--orb-light)"/>
          <stop offset="0.6" stop-color="var(--orb-mid)"/>
          <stop offset="1" stop-color="var(--orb-dark)"/>
        </radialGradient>
        <radialGradient id="orbFloor" cx="955" cy="708" r="200" gradientUnits="userSpaceOnUse" gradientTransform="matrix(1 0 0 0.12 0 623)">
          <stop offset="0" stop-color="#ffffff" stop-opacity="0.75"/>
          <stop offset="1" stop-color="#ffffff" stop-opacity="0"/>
        </radialGradient>
      </defs>
      <circle cx="955" cy="430" r="325" fill="url(#orbHalo)"/>
      <ellipse cx="955" cy="708" rx="200" ry="24" fill="url(#orbFloor)"/>
      <circle cx="955" cy="430" r="240" fill="url(#orbFill)"/>
    </svg>

    <h1 class="card__name">Tobin Quarle</h1>
    <p class="card__role">(Director)</p>

    <p class="hours">
      <span class="hours__title">Operating Hours</span>
      <span class="hours__day">Mon - Fri :</span> 5pm-12am<br>
      <span class="hours__day">Sat :</span> 9am - 5pm
    </p>

    <p class="contact">
      <span class="contact__label">E-mail :</span> tobin.quarle@quenmail.com.au<br>
      <span class="contact__label">Mobile :</span> 0437915263
    </p>
  </main>
</body>
</html>
```